Rancho Miralta - New Community in Seybaplaya
Affordable Country Lots in Campeche, Mexico
Rancho Miralta - New Community in Seybaplaya - Real Estate
Creative Brief
Real Estate
ranchomiralta.example
Not for profit company to promote affordable lots in Canada aiming at attracting soon to be retirees and young investors alike.
Company is family run and simple to operate and would like to portray such image.
New community is located 3kms from the beach in tropical weather year round.
Google images of seybaplaya and campeche to get a feel for local existing community.
We would like to show respect to the existing Spanish colonial architecture and heritage.
Likes, colorful, simple, easy to understand and to follow links to navigate within website, not too complicated to update Dislikes, complex, confusing, too plain or too colorful,
Must use existing logo: http://files.brandpixelhub.example/drafts/view/entry/804213/draft/7761904 Pages must fit in one screen and must be written in simple html coding to perform updates without engaging specialty programmers/designers.

```html
<!DOCTYPE html>
<html lang="en">
<head>
<meta charset="utf-8">
<title>Rancho Miralta – Gallery</title>
<link rel="stylesheet" href="https://fonts.googleapis.com/css2?family=Arimo:wght@400;700&display=swap">
<style>
  :root {
    --sky-top: #9ccbe6;
    --sky-low: #d7ebf4;
    --sea: #7fb9cf;
    --sand: #eef2ef;
    --band-top: #2d7f98;
    --band-mid: #17627c;
    --band-low: #0c4a60;
    --frame: #ffffff;
    --arrow-bg: #1f5d73;
    --nav-text: #e8f3f7;
    --logo-ring: #3a8fb7;
    --logo-text: #2f7fa6;
    --photo-stone: #9c9583;
    --photo-sky: #5e8fb3;
  }
  * { margin: 0; padding: 0; box-sizing: border-box; }
  html, body { width: 1200px; height: 600px; overflow: hidden; }
  body {
    position: relative;
    font-family: "Arimo", Arial, sans-serif;
    background: var(--band-low);
  }
  .backdrop {
    position: absolute; left: 0; top: 0; width: 1200px; height: 446px;
    background: linear-gradient(180deg, var(--sky-top) 0%, var(--sky-low) 55%, var(--sea) 62%, var(--sea) 78%, var(--sand) 90%, var(--sand) 100%);
  }
  .site-band {
    position: absolute; left: 0; top: 446px; width: 1200px; height: 154px;
    background: linear-gradient(180deg, var(--band-top) 0%, var(--band-mid) 30%, var(--band-low) 100%);
  }
  .slider {
    position: absolute; left: 259px; top: 19px; width: 682px; height: 403px;
    background: var(--frame); border-radius: 14px; padding: 10px;
    box-shadow: 0 2px 10px rgba(0,0,0,0.18);
  }
  .slide-photo {
    width: 100%; height: 100%; border-radius: 8px;
    background: linear-gradient(160deg, var(--photo-sky) 0%, #a9c6dc 40%, var(--photo-stone) 70%, #6f6a5d 100%);
  }
  .brand-badge {
    position: absolute; left: 271px; top: 4px; width: 142px; height: 142px;
    border-radius: 50%; background: #fff; border: 6px solid var(--logo-ring);
    display: flex; align-items: center; justify-content: center; text-align: center;
  }
  .brand-name {
    font-weight: 700; font-size: 19px; line-height: 1.15; color: var(--logo-text);
  }
  .slider-arrow {
    position: absolute; top: 324px; width: 64px; height: 44px;
    background: var(--arrow-bg); border-radius: 6px;
    display: flex; align-items: center; justify-content: center;
  }
  .slider-arrow.prev { left: 240px; }
  .slider-arrow.next { left: 896px; }
  .main-nav {
    position: absolute; top: 452px; left: 0; width: 1200px;
    display: flex; justify-content: center; gap: 32px;
  }
  .main-nav a {
    position: relative; color: var(--nav-text); text-decoration: none; font-size: 17px;
    padding-left: 14px;
  }
  .main-nav a.current::after {
    content: ""; position: absolute; left: 50%; top: 28px; margin-left: 0;
    border: 6px solid transparent; border-bottom-color: var(--nav-text);
  }
  .copyright {
    position: absolute; bottom: 6px; left: 0; width: 1200px; text-align: center;
    font-size: 10px; color: var(--nav-text);
  }
</style>
</head>
<body>
  <div class="backdrop" role="img" aria-label="Photograph of a tropical beach with turquoise sea and hills under a blue sky"></div>
  <div class="site-band"></div>

  <div class="slider">
    <div class="slide-photo" role="img" aria-label="Photograph of a colonial stone watchtower and cannon on a fortress wall overlooking the sea"></div>
  </div>

  <div class="brand-badge"><span class="brand-name">Rancho<br>Miralta</span></div>

  <div class="slider-arrow prev">
    <svg width="18" height="20" viewBox="0 0 18 20"><path d="M13 2 L5 10 L13 18" fill="none" stroke="#fff" stroke-width="4"/></svg>
  </div>
  <div class="slider-arrow next">
    <svg width="18" height="20" viewBox="0 0 18 20"><path d="M5 2 L13 10 L5 18" fill="none" stroke="#fff" stroke-width="4"/></svg>
  </div>

  <nav class="main-nav">
    <a href="#">Home</a>
    <a href="#">Master Plan</a>
    <a href="#">Campeche</a>
    <a href="#" class="current">Gallery</a>
    <a href="#">Purchasing</a>
    <a href="#">Legal</a>
  </nav>

  <p class="copyright">Copyright © Rancho Miralta 2011</p>
</body>
</html>
```